LED Bulb Packaging

We require a retail box design so some led lighting. The concept must be uniform accross a nuimber of sizes with technical information and Actual bulb image replaceable.

```html
<!DOCTYPE html>
<html lang="en">
<head>
<meta charset="utf-8">
<title>LED Corn Light – Retail Box Dieline</title>
<link rel="stylesheet" href="https://fonts.googleapis.com/css2?family=Oswald:wght@500;600&family=Roboto+Condensed:wght@400;700&display=swap">
<style>
  :root{
    --paper:#ffffff;
    --dieline:#f2a3a3;
    --glue-line:#e0252b;
    --brand-red:#e8413a;
    --brand-orange:#f7941d;
    --ink:#111111;
    --tag-green:#8bc540;
    --tag-grey:#bcbdc0;
    --tag-blue:#8ecff2;
    --icon-green:#6dbf4b;
    --photo-dark:#3b3f44;
    --photo-light:#e4e8ea;
  }
  html,body{margin:0;padding:0;overflow:hidden;background:var(--paper);}
  .canvas{display:block;width:1200px;height:504px;}
  .die{fill:none;stroke:var(--dieline);stroke-width:1;}
  .glue-flap{fill:none;stroke:var(--glue-line);stroke-width:2;}
  .led-word{font-family:"Oswald",sans-serif;font-weight:600;fill:var(--brand-red);}
  .corn-word{font-family:"Roboto Condensed",sans-serif;fill:var(--ink);}
  .tag-text{font-family:"Roboto Condensed",sans-serif;font-weight:700;fill:#fff;font-size:8px;}
  .tag-sub{font-family:"Roboto Condensed",sans-serif;fill:#fff;font-size:4px;}
  .note-title{font-family:"Roboto Condensed",sans-serif;font-weight:700;fill:var(--brand-red);font-size:7px;}
  .note-line{font-family:"Roboto Condensed",sans-serif;fill:var(--ink);font-size:6.6px;}
  .watt{font-family:"Oswald",sans-serif;font-weight:500;fill:var(--brand-red);font-size:62px;}
  .spec-bar-text{font-family:"Roboto Condensed",sans-serif;fill:#fff;font-size:5px;}
  .feature-card{fill:#fff;}
  .feature-icon{fill:var(--icon-green);}
  .feature-label{font-family:"Roboto Condensed",sans-serif;fill:var(--ink);font-size:4px;}
  .cert-badge{fill:#fff;}
  .energy-letter{font-family:"Roboto Condensed",sans-serif;font-weight:700;fill:#fff;font-size:5px;}
</style>
</head>
<body>
<svg class="canvas" viewBox="0 0 1380 580" xmlns="http://www.w3.org/2000/svg">
  <defs>
    <linearGradient id="band-red-orange" x1="0" x2="1">
      <stop offset="0" stop-color="var(--brand-red)"/>
      <stop offset="0.45" stop-color="var(--brand-orange)"/>
      <stop offset="1" stop-color="var(--brand-orange)"/>
    </linearGradient>
    <linearGradient id="band-orange-red" x1="0" x2="1">
      <stop offset="0" stop-color="var(--brand-orange)"/>
      <stop offset="1" stop-color="var(--brand-red)"/>
    </linearGradient>
    <linearGradient id="bulb-tone" x1="0" x2="1">
      <stop offset="0" stop-color="var(--photo-dark)"/>
      <stop offset="0.15" stop-color="#9ea4a8"/>
      <stop offset="0.5" stop-color="var(--photo-light)"/>
      <stop offset="0.85" stop-color="#9ea4a8"/>
      <stop offset="1" stop-color="var(--photo-dark)"/>
    </linearGradient>
    <clipPath id="front-panel-a"><rect x="85" y="245" width="460" height="175"/></clipPath>
    <clipPath id="front-panel-b"><rect x="720" y="245" width="463" height="175"/></clipPath>
  </defs>

  <!-- Dieline -->
  <g class="dieline">
    <rect class="die" x="85" y="245" width="1270" height="175"/>
    <line class="die" x1="545" y1="245" x2="545" y2="420"/>
    <line class="die" x1="720" y1="245" x2="720" y2="420"/>
    <line class="die" x1="1183" y1="245" x2="1183" y2="420"/>
    <path class="glue-flap" d="M85,245 L37,262 L37,405 L85,420"/>
    <path class="die" d="M85,245 L165,155 H455 L545,245"/>
    <path class="die" d="M220,238 H410 V246 M275,238 V218 Q275,210 283,210 H342 Q350,210 350,218 V238 M275,246 V277 Q275,285 283,285 H342 Q350,285 350,277 V246"/>
    <path class="die" d="M545,245 L625,160 H720"/>
    <path class="die" d="M720,245 V100 H858 V45 Q858,25 878,25 H1020 Q1040,25 1040,45 V100 H1183 V245"/>
    <path class="die" d="M858,72 H900 V80 Q950,90 995,80 V72 H1040"/>
    <path class="die" d="M1183,245 V155 H1270 L1355,245"/>
    <path class="die" d="M85,420 L200,510 V545 Q200,555 210,555 H420 Q430,555 430,545 V510 L545,420"/>
    <path class="die" d="M545,420 L625,505 H720"/>
    <path class="die" d="M720,420 V470 L790,505 H835 V555 H1040 V505 H1100 L1183,470"/>
    <path class="die" d="M1183,420 L1270,505 V550 H1340 L1355,535 V420"/>
  </g>

  <!-- Top flap of front panel A -->
  <g class="top-flap-a">
    <rect x="160" y="161" width="300" height="5" fill="url(#band-red-orange)"/>
    <text class="led-word" x="310" y="196" font-size="26" text-anchor="middle">LED</text>
    <text class="corn-word" x="310" y="205" font-size="7" text-anchor="middle">CORN LIGHT</text>
  </g>
  <rect x="625" y="160" width="95" height="5" fill="var(--brand-orange)"/>

  <!-- Front panel A -->
  <g class="front-panel front-panel-a" clip-path="url(#front-panel-a)">
    <g role="img" aria-label="Product photo of the LED corn light bulb">
      <rect x="-70" y="-230" width="140" height="420" rx="14" fill="url(#bulb-tone)" transform="translate(440,360) rotate(-38)"/>
    </g>
    <rect x="85" y="385" width="460" height="35" fill="url(#band-red-orange)"/>
  </g>
  <g class="spec-tags" transform="translate(85,0)">
    <path d="M0,274 H68 L76,282 L68,290 H0Z" fill="var(--ink)"/>
    <text class="tag-text" x="34" y="282" text-anchor="middle">120ML/W</text>
    <text class="tag-sub" x="34" y="288" text-anchor="middle">Luminous Efficiency</text>
    <path d="M0,297 H68 L76,305 L68,313 H0Z" fill="var(--tag-green)"/>
    <text class="tag-text" x="34" y="305" text-anchor="middle">50000 HRS</text>
    <text class="tag-sub" x="34" y="311" text-anchor="middle">Lifespan</text>
    <path d="M0,320 H68 L76,328 L68,336 H0Z" fill="var(--tag-grey)"/>
    <text class="tag-text" x="34" y="328" text-anchor="middle">85%</text>
    <text class="tag-sub" x="34" y="334" text-anchor="middle">Up To Energy Saving</text>
    <path d="M0,343 H68 L76,351 L68,359 H0Z" fill="var(--tag-blue)"/>
    <text class="tag-text" x="34" y="354" text-anchor="middle">IP64</text>
  </g>
  <text class="led-word" x="238" y="346" font-size="66" text-anchor="middle">LED</text>
  <text class="corn-word" x="238" y="357" font-size="12" text-anchor="middle">CORN LIGHT</text>
  <g class="cert-row">
    <circle class="cert-badge" cx="181" cy="398" r="6"/><circle class="cert-badge" cx="207" cy="396" r="6"/>
    <rect class="cert-badge" x="225" y="390" width="12" height="12"/><circle class="cert-badge" cx="254" cy="396" r="6"/>
    <circle class="cert-badge" cx="276" cy="396" r="6"/><rect class="cert-badge" x="290" y="390" width="14" height="12"/>
  </g>

  <!-- Side panel: notes and energy rating -->
  <g class="side-panel-notes">
    <text class="note-title" x="556" y="263">NOTE:</text>
    <text class="note-line" x="556" y="273">· Before install or replace the lamps please cut off</text>
    <text class="note-line" x="559" y="281">the switch.</text>
    <text class="note-line" x="556" y="289">· After installed,when lamp work normal,pls note</text>
    <text class="note-line" x="559" y="297">not take off the driver with electriferous.</text>
    <text class="note-line" x="556" y="305">· After lighting a long time,the lamps can be reach</text>
    <text class="note-line" x="559" y="313">60°C,Pls be careful to take off the lamps avoid scald.</text>
    <text class="note-line" x="556" y="321">· Interior driver is constant current.</text>
    <text class="note-line" x="556" y="329">· Work temperature is -20~40°C.</text>
    <g class="energy-rating">
      <rect x="555" y="340" width="57" height="70" fill="none" stroke="var(--ink)" stroke-width="0.8"/>
      <rect x="556" y="341" width="28" height="10" fill="var(--tag-grey)"/>
      <rect x="597" y="341" width="14" height="9" fill="#2b4c9b"/>
      <line x1="595" y1="351" x2="595" y2="409" stroke="var(--ink)" stroke-width="0.8"/>
      <path d="M557,355 H568 L571,359 L568,363 H557Z" fill="#0a9d47"/><text class="energy-letter" x="559" y="361">A</text>
      <path d="M557,364 H572 L575,368 L572,372 H557Z" fill="#52b848"/><text class="energy-letter" x="559" y="370">B</text>
      <path d="M557,373 H576 L579,377 L576,381 H557Z" fill="#bfd730"/><text class="energy-letter" x="559" y="379">C</text>
      <path d="M557,382 H580 L583,386 L580,390 H557Z" fill="#fff200"/><text class="energy-letter" x="559" y="388">D</text>
      <path d="M557,391 H584 L587,395 L584,399 H557Z" fill="#fbb040"/><text class="energy-letter" x="559" y="397">E</text>
      <path d="M557,400 H588 L591,404 L588,408 H557Z" fill="#ef4136"/><text class="energy-letter" x="559" y="406">F</text>
      <path d="M611,353 H600 L597,357 L600,361 H611Z" fill="var(--ink)"/><text class="energy-letter" x="603" y="359">A</text>
    </g>
  </g>

  <!-- Top flap of front panel B (prints inverted) -->
  <g class="feature-band">
    <rect x="720" y="105" width="463" height="55" fill="url(#band-orange-red)"/>
    <g transform="rotate(180 953 132)">
      <g transform="translate(796,112)">
        <rect class="feature-card" width="34" height="40"/><circle class="feature-icon" cx="17" cy="12" r="7"/>
        <text class="feature-label" x="17" y="28" text-anchor="middle">High</text><text class="feature-label" x="17" y="33" text-anchor="middle">Brightness</text>
      </g>
      <g transform="translate(838,112)">
        <rect class="feature-card" width="34" height="40"/><circle class="feature-icon" cx="17" cy="12" r="7"/>
        <text class="feature-label" x="17" y="30" text-anchor="middle">Longlife</text>
      </g>
      <g transform="translate(880,112)">
        <rect class="feature-card" width="34" height="40"/><circle class="feature-icon" cx="17" cy="12" r="7"/>
        <text class="feature-label" x="17" y="30" text-anchor="middle">Security</text>
      </g>
      <g transform="translate(922,112)">
        <rect class="feature-card" width="34" height="40"/><circle class="feature-icon" cx="17" cy="12" r="7"/>
        <text class="feature-label" x="17" y="28" text-anchor="middle">Energy</text><text class="feature-label" x="17" y="33" text-anchor="middle">Saving</text>
      </g>
      <g transform="translate(964,112)">
        <rect class="feature-card" width="34" height="40"/><circle class="feature-icon" cx="17" cy="12" r="7"/>
        <text class="feature-label" x="17" y="28" text-anchor="middle">Protect</text><text class="feature-label" x="17" y="33" text-anchor="middle">Your Eyes</text>
      </g>
      <g transform="translate(1006,112)">
        <rect class="feature-card" width="34" height="40"/><circle class="feature-icon" cx="17" cy="12" r="7"/>
        <text class="feature-label" x="17" y="28" text-anchor="middle">Low carbon</text><text class="feature-label" x="17" y="33" text-anchor="middle">Green</text>
      </g>
      <g transform="translate(1048,112)">
        <rect class="feature-card" width="34" height="40"/><circle cx="17" cy="12" r="7" fill="none" stroke="#ccc" stroke-width="0.6"/>
        <text class="feature-label" x="17" y="28" text-anchor="middle">No</text><text class="feature-label" x="17" y="33" text-anchor="middle">Flicker Free</text>
      </g>
      <g transform="translate(1090,112)">
        <rect class="feature-card" width="34" height="40"/><circle class="feature-icon" cx="17" cy="12" r="7"/>
        <text class="feature-label" x="17" y="28" text-anchor="middle">No</text><text class="feature-label" x="17" y="33" text-anchor="middle">Radiation</text>
      </g>
    </g>
    <g transform="rotate(180 953 200)">
      <text class="led-word" x="953" y="214" font-size="44" text-anchor="middle">LED</text>
      <text class="corn-word" x="953" y="225" font-size="10" text-anchor="middle">CORN LIGHT</text>
    </g>
  </g>

  <!-- Front panel B -->
  <g class="front-panel front-panel-b" clip-path="url(#front-panel-b)">
    <g role="img" aria-label="Product photo of the LED corn light bulb">
      <rect x="-70" y="-230" width="140" height="420" rx="14" fill="url(#bulb-tone)" transform="translate(1050,330) rotate(-38)"/>
    </g>
    <rect x="720" y="385" width="463" height="35" fill="url(#band-red-orange)"/>
  </g>
  <g class="spec-tags" transform="translate(720,0)">
    <path d="M0,274 H68 L76,282 L68,290 H0Z" fill="var(--ink)"/>
    <text class="tag-text" x="34" y="282" text-anchor="middle">120ML/W</text>
    <text class="tag-sub" x="34" y="288" text-anchor="middle">Luminous Efficiency</text>
    <path d="M0,297 H68 L76,305 L68,313 H0Z" fill="var(--tag-green)"/>
    <text class="tag-text" x="34" y="305" text-anchor="middle">50000 HRS</text>
    <text class="tag-sub" x="34" y="311" text-anchor="middle">Lifespan</text>
    <path d="M0,320 H68 L76,328 L68,336 H0Z" fill="var(--tag-grey)"/>
    <text class="tag-text" x="34" y="328" text-anchor="middle">85%</text>
    <text class="tag-sub" x="34" y="334" text-anchor="middle">Up To Energy Saving</text>
    <path d="M0,343 H68 L76,351 L68,359 H0Z" fill="var(--tag-blue)"/>
    <text class="tag-text" x="34" y="354" text-anchor="middle">IP64</text>
  </g>
  <text class="led-word" x="873" y="346" font-size="66" text-anchor="middle">LED</text>
  <text class="corn-word" x="873" y="357" font-size="12" text-anchor="middle">CORN LIGHT</text>
  <g class="cert-row">
    <circle class="cert-badge" cx="813" cy="398" r="6"/><circle class="cert-badge" cx="840" cy="396" r="6"/>
    <rect class="cert-badge" x="858" y="390" width="12" height="12"/><circle class="cert-badge" cx="887" cy="396" r="6"/>
    <circle class="cert-badge" cx="910" cy="396" r="6"/><rect class="cert-badge" x="925" y="390" width="14" height="12"/>
  </g>

  <!-- Side panel: wattage -->
  <g class="side-panel-watt">
    <text class="watt" x="1269" y="348" text-anchor="middle">27W</text>
    <rect x="1220" y="355" width="96" height="9" fill="var(--ink)"/>
    <text class="spec-bar-text" x="1268" y="361.5" text-anchor="middle">50000 hrs   IP64   1800lm</text>
  </g>
</svg>
</body>
</html>
```